eCard to send to Realtors (real estate, professional)

We are a title insurance company which falls under the category of financial services. We are looking for someone to design an ecard that may be emailed to Realtors. The purpose of the card is to congratulate them on their new real estate listing. This means a house or condo has just been placed onto the market for sale. We'd like it to be professional but also fun and eye catching. Our colors are black, white and maroon but we can print the logo or our esignature in b/w only. Thanks!
Target Market(s)
Real estate agents, Realtors
Industry/Entity Type
Real Estate
Requirements
Nice to have
- It would be nice to have the ability to insert the clients name into this card. It would also be nice if the card is able to be imported into Constant Contact.

```html
<!DOCTYPE html>
<html lang="en">
<head>
<meta charset="utf-8">
<title>New Listing eCard – Harlow Title &amp; Escrow Company</title>
<link href="https://fonts.googleapis.com/css2?family=Montserrat:wght@300;400;700;800&display=swap" rel="stylesheet">
<style>
  :root {
    --backdrop: #3b3b3b;
    --maroon-light: #b81f27;
    --maroon: #9a161d;
    --maroon-deep: #5e0c10;
    --white: #ffffff;
    --green: #2fb34a;
    --logo-ink: #7a1419;
    --roof-dark: #141414;
    --roof-grey: #a8a9ad;
  }
  * { margin: 0; padding: 0; box-sizing: border-box; }
  html, body {
    width: 1200px; height: 894px; overflow: hidden;
    background: var(--backdrop);
    font-family: "Montserrat", sans-serif;
  }
  .ecard {
    position: absolute; left: 40px; top: 64px;
    width: 1120px; height: 766px;
    border-radius: 38px;
    overflow: hidden;
    background: radial-gradient(ellipse 70% 65% at 55% 45%, var(--maroon-light) 0%, var(--maroon) 55%, var(--maroon-deep) 100%);
    color: var(--white);
  }
  .headline {
    position: absolute; top: 22px; left: 0; width: 100%;
    text-align: center;
    font-weight: 800; font-size: 92px; line-height: 1;
    letter-spacing: -0.5px;
  }
  .subhead {
    position: absolute; top: 122px; left: 0; width: 100%;
    text-align: center;
    font-weight: 300; font-size: 50px; line-height: 1;
    color: var(--green);
  }
  .roof-art {
    position: absolute; left: 110px; top: 192px;
    width: 900px; height: 160px;
    border-radius: 6px;
    background: linear-gradient(90deg, var(--roof-dark) 0%, #4a4a4c 45%, var(--roof-grey) 60%, var(--roof-grey) 100%);
  }
  .houses-row {
    position: absolute; left: 84px; top: 384px;
    width: 961px; height: 82px;
    background: linear-gradient(90deg, #86a23a 0%, #e2533a 12%, #4b80c9 23%, #d4a64a 34%, #6bbfe0 45%, #f2b92a 56%, #86a23a 67%, #4b80c9 78%, #ef7d7d 89%, #f0632d 100%);
    border-radius: 6px;
  }
  .tagline {
    position: absolute; top: 480px; left: 0; width: 100%;
    text-align: center;
    font-weight: 700; font-size: 30px; line-height: 1.2;
    color: var(--green);
  }
  .brand-badge {
    position: absolute; left: -70px; top: 552px;
    width: 540px; height: 290px;
    border-radius: 50%;
    background: var(--white);
    box-shadow: 6px -4px 0 4px var(--maroon-deep);
  }
  .brand-name {
    position: absolute; left: 20px; top: 640px;
    width: 420px;
    text-align: center;
    font-weight: 700; font-size: 30px; line-height: 1.2;
    color: var(--logo-ink);
    text-transform: uppercase;
    white-space: nowrap;
  }
  .contact {
    position: absolute; left: 520px; top: 620px;
    width: 560px; text-align: center;
  }
  .contact-phone {
    display: block;
    font-weight: 300; font-size: 72px; line-height: 1;
  }
  .contact-web {
    display: block; margin-top: 18px;
    font-weight: 400; font-size: 31px; line-height: 1;
    letter-spacing: 5px;
  }
  .contact-web strong { font-weight: 700; }
</style>
</head>
<body>
  <main class="ecard">
    <h1 class="headline">Congratulations</h1>
    <p class="subhead">on your new real estate listing</p>

    <div class="roof-art" role="img" aria-label="Large house roof illustration in black and grey"></div>
    <div class="houses-row" role="img" aria-label="Row of ten small colourful house icons"></div>

    <p class="tagline">A successful closing starts with a solid foundation ...</p>

    <div class="brand-badge"></div>
    <p class="brand-name">Harlow Title<br>&amp; Escrow Company</p>

    <div class="contact">
      <span class="contact-phone">(555) 014 2290</span>
      <span class="contact-web">www.<strong>harlowtitle</strong>.com</span>
    </div>
  </main>
</body>
</html>
```